Prepared ready to cook meal delivery service needs a flyer design

We need a flyer design for a startup company based in Cape Town, South Africa. I've attached a few flyer designs that I like.

The company is called 'Brindle' and our website will be found at brindle.co.za. We don't have a logo yet.

Flyer text:

Brindle
Ready to roast

Do you feel like a home cooked meal but don't like shopping, peeling, chopping, cooking, or cleaning up?

We deliver ready to roast free range chicken and fresh vegetables to your door.

To order: SMS your name to 083 614 2958 and we'll call you back.

Only the best ingredients used
Free range chickens. Fresh herbs and vegetables. Virgin olive oil.

No bad carbs!

Ready to roast Free range chicken and fresh veggies
For 2 R99
For 4 R139
Updates

Wording of flyer updated.

Target Market(s)

Local Cape Townians that hate grocery shopping and need help saving time preparing meals.

Industry/Entity Type

Delivery Service

Requirements
Must have
• To find out more: SMS your name to 083 614 2958

```html
<!DOCTYPE html>
<html lang="en">
<head>
<meta charset="utf-8">
<title>Brindle – ready to roast</title>
<link rel="stylesheet" href="https://fonts.googleapis.com/css2?family=Quicksand:wght@500;600;700&display=swap">
<style>
  :root {
    --red-deep: #8e0d12;
    --red: #c4161c;
    --red-bright: #d9262b;
    --cream: #f3f0c6;
    --green: #5d7f12;
    --ink: #161616;
    --order-red: #b3141a;
    --white: #ffffff;
    --food-warm: #a8542a;
    --food-dark: #6e3a1e;
    --photo-light: #e9dcc6;
    --photo-warm: #cfa46e;
  }
  * { box-sizing: border-box; margin: 0; padding: 0; }
  html, body { width: 927px; height: 1200px; overflow: hidden; background: #ffffff; }
  body { font-family: "Quicksand", "Trebuchet MS", sans-serif; }

  .flyer {
    position: relative;
    width: 927px;
    height: 1200px;
    overflow: hidden;
    background: var(--red);
  }

  .food-backdrop {
    position: absolute;
    inset: 0;
    background: linear-gradient(180deg, var(--red-deep) 0%, var(--red) 14%, var(--red) 24%, var(--food-warm) 55%, var(--food-dark) 100%);
  }

  .brand {
    position: absolute;
    top: 28px; left: 0; width: 927px;
    text-align: center;
    color: var(--cream);
    font-weight: 700;
  }
  .brand-name { font-size: 108px; line-height: 1; letter-spacing: 1px; }
  .brand-tagline { font-size: 40px; line-height: 1; margin-top: 2px; }

  .panel {
    position: absolute;
    left: 100px; top: 211px;
    width: 727px; height: 886px;
    background: var(--white);
  }

  .intro, .delivery, .quality, .order {
    position: absolute;
    left: 100px; width: 727px;
    text-align: center;
  }
  .intro {
    top: 246px;
    color: var(--ink);
    font-size: 29px;
    font-weight: 500;
    line-height: 34px;
  }
  .delivery {
    top: 390px;
    color: var(--green);
    font-size: 25px;
    font-weight: 600;
    line-height: 33px;
  }

  .offer-band {
    position: absolute;
    left: 0; top: 572px;
    width: 927px; height: 182px;
    background: linear-gradient(180deg, var(--red-bright) 0%, var(--red) 55%, var(--red-deep) 100%);
    box-shadow: 0 4px 10px rgba(0,0,0,0.35);
  }
  .offer-label {
    position: absolute;
    left: 0; top: 610px; width: 213px;
    text-align: right;
    color: var(--white);
    font-size: 22px;
    font-weight: 600;
    line-height: 27px;
  }
  .price-list {
    position: absolute;
    left: 710px; top: 618px;
    color: var(--white);
    font-weight: 700;
    list-style: none;
  }
  .price-list li { display: flex; align-items: baseline; line-height: 1.15; }
  .price-list .serves { font-size: 27px; }
  .price-list .serves b { font-size: 40px; font-weight: 700; margin-right: 16px; }
  .price-list .price { font-size: 27px; }
  .price-list .price b { font-size: 42px; font-weight: 700; }

  .dish-photo {
    position: absolute;
    left: 238px; top: 494px;
    width: 455px; height: 331px;
    border-radius: 14px;
    border: 6px solid var(--white);
    box-shadow: 0 4px 12px rgba(0,0,0,0.4);
    background: linear-gradient(180deg, var(--photo-light) 0%, var(--photo-warm) 100%);
  }

  .quality {
    top: 851px;
    color: var(--green);
    font-size: 25px;
    font-weight: 600;
    line-height: 34px;
  }
  .order {
    top: 985px;
    color: var(--order-red);
    font-size: 26px;
    font-weight: 700;
    line-height: 34px;
  }

  .website {
    position: absolute;
    left: 0; top: 1148px; width: 927px;
    text-align: center;
    color: var(--cream);
    font-size: 26px;
    font-weight: 700;
    text-shadow: 0 2px 3px rgba(0,0,0,0.5);
  }
</style>
</head>
<body>
  <main class="flyer">
    <div class="food-backdrop" role="img" aria-label="Photograph of roasted chicken, red peppers, onions, lemons and fresh herbs"></div>

    <header class="brand">
      <div class="brand-name">Brindle</div>
      <div class="brand-tagline">ready to roast</div>
    </header>

    <section class="panel"></section>

    <p class="intro">Do you feel like a home cooked meal but<br>don’t like shopping, peeling, chopping,<br>cooking, or cleaning up?</p>
    <p class="delivery">We deliver ready to roast free range chicken<br>and fresh vegetables to your door.</p>

    <div class="offer-band"></div>
    <p class="offer-label">Ready to roast<br>Free range<br>chicken and<br>fresh veggies</p>
    <ul class="price-list">
      <li><span class="serves">for<b>2</b></span><span class="price">R<b>99</b></span></li>
      <li><span class="serves">for<b>4</b></span><span class="price">R<b>139</b></span></li>
    </ul>

    <div class="dish-photo" role="img" aria-label="Photograph of a whole roast chicken with peppers, onions, potatoes and lemon in a white dish"></div>

    <p class="quality">Only the best ingredients used.<br>Free range chickens. Fresh herbs and vegetables.<br>Virgin olive oil. No bad carbs!</p>
    <p class="order">To order: SMS your name to 083 614 2958<br>and we’ll call you back</p>

    <footer class="website">www.brindle.co.za</footer>
  </main>
</body>
</html>
```